Business card design for new brand

We have recently rebranded and need a new business card template.

We are an insurance underwriting agency. All of our products are sold via other partner companies, so these are just to pass on our details to other organisations.

We would like to see designs that use the colour green (current stationary generally uses lime green (rgb 142,190,63) and forest green (0,154,79) to comply with our logo's colours. We are happy with other shades of green.

Business cards need to include our logo, as well as space for:
1. Full name
2. Qualifications (optional)
3. Title
4. Office number
5. Mobile number
6. Email address

Our logo is enclosed here.

```html
<!DOCTYPE html>
<html lang="en">
<head>
<meta charset="utf-8">
<title>Verdant Cover business card</title>
<link rel="stylesheet" href="https://fonts.googleapis.com/css2?family=Lato:wght@400;700&display=swap">
<style>
  :root {
    --page: #d9d9d9;
    --card-dark: #1c1c1c;
    --card-dark-edge: #262626;
    --card-light: #ececec;
    --forest: #00582c;
    --green: #009a4f;
    --lime: #8ebe3f;
    --ink: #2e2e2e;
    --white: #ffffff;
  }
  * { box-sizing: border-box; margin: 0; padding: 0; }
  html, body { width: 1200px; height: 800px; overflow: hidden; }
  body {
    background: var(--page);
    font-family: "Lato", sans-serif;
    position: relative;
  }
  .card {
    position: absolute;
    left: 320px;
    width: 560px;
    height: 320px;
    box-shadow: 0 6px 18px rgba(0,0,0,0.18);
  }
  .card--back { top: 65px; }
  .card--front { top: 415px; background: var(--card-light); }

  .back-texture {
    position: absolute; inset: 0;
    background: radial-gradient(ellipse at 50% 35%, var(--card-dark-edge) 0%, var(--card-dark) 70%);
  }
  .brand {
    display: flex; align-items: center; gap: 10px;
    font-family: "Lato", sans-serif;
    font-weight: 700;
    white-space: nowrap;
  }
  .brand-mark { width: 22px; height: 22px; background: var(--green); flex: none; }
  .brand-name { font-size: 30px; }
  .card--back .brand {
    position: absolute; left: 0; right: 0; top: 140px;
    justify-content: center;
  }
  .card--back .brand-name { color: var(--white); }
  .card--front .brand { position: absolute; left: 36px; top: 40px; }
  .card--front .brand-name { color: var(--ink); font-size: 28px; }

  .person { position: absolute; left: 37px; top: 160px; right: 40px; }
  .person-name { color: var(--forest); font-weight: 700; font-size: 18px; }
  .person-role { display: flex; align-items: flex-end; gap: 8px; margin-top: 2px; }
  .person-title { color: var(--ink); font-size: 15px; }
  .person-rule { flex: 1; height: 1px; background: var(--forest); margin-bottom: 5px; }

  .contacts { position: absolute; left: 37px; top: 228px; list-style: none; }
  .contacts li {
    display: flex; align-items: center; gap: 10px;
    font-size: 13.5px; color: var(--ink); height: 20px;
  }
  .contacts svg { width: 15px; height: 15px; fill: var(--lime); flex: none; }

  .address {
    position: absolute; right: 38px; top: 228px;
    font-style: normal; text-align: right;
    font-size: 13.5px; line-height: 20px; color: var(--ink);
  }
</style>
</head>
<body>
  <section class="card card--back">
    <div class="back-texture" role="img" aria-label="Subtle dark hexagon texture"></div>
    <div class="brand">
      <span class="brand-mark"></span>
      <span class="brand-name">Verdant Cover Pty Ltd</span>
    </div>
  </section>

  <section class="card card--front">
    <div class="brand">
      <span class="brand-mark"></span>
      <span class="brand-name">Verdant Cover Pty Ltd</span>
    </div>

    <div class="person">
      <p class="person-name">Sam Ridley, M.Ed.</p>
      <div class="person-role">
        <span class="person-title">Managing Director</span>
        <span class="person-rule"></span>
      </div>
    </div>

    <ul class="contacts">
      <li>
        <svg viewBox="0 0 24 24" aria-hidden="true"><path d="M6.6 10.8a15.1 15.1 0 0 0 6.6 6.6l2.2-2.2a1 1 0 0 1 1-.25 11.4 11.4 0 0 0 3.6.57 1 1 0 0 1 1 1V20a1 1 0 0 1-1 1A17 17 0 0 1 3 4a1 1 0 0 1 1-1h3.5a1 1 0 0 1 1 1c0 1.25.2 2.45.57 3.57a1 1 0 0 1-.25 1z"/></svg>
        +61 (02) 5550 1843
      </li>
      <li>
        <svg viewBox="0 0 24 24" aria-hidden="true"><path d="M8 1h8a2 2 0 0 1 2 2v18a2 2 0 0 1-2 2H8a2 2 0 0 1-2-2V3a2 2 0 0 1 2-2zm0 3v14h8V4zm4 15.5a1 1 0 1 0 0 2 1 1 0 0 0 0-2z"/></svg>
        +61 (0) 455 018 327
      </li>
      <li>
        <svg viewBox="0 0 24 24" aria-hidden="true"><path d="M2 5h20v14H2zm2 2v.5l8 5.5 8-5.5V7zm0 3v7h16v-7l-8 5.5z"/></svg>
        sam.ridley@au.verdantcover.ltd
      </li>
    </ul>

    <address class="address">
      Level 14, Harbour Point,<br>
      58 Ferris Lane,<br>
      Northbridge NSW 2063
    </address>
  </section>
</body>
</html>
```